Design a Website Mockup for Car Rental "MOBILE ONLY"

Hi,

I want to design a mobile version for the attached images.
Please use the same information and same colors.

Good luck!
TIBUR

```html
<!DOCTYPE html>
<html lang="en">
<head>
<meta charset="utf-8">
<title>Car Rental – Booking Step 1</title>
<link href="https://fonts.googleapis.com/css2?family=Arimo:wght@400;700&display=swap" rel="stylesheet">
<style>
:root{
  --page-bg:#ffffff;
  --card-border:#d9d9d9;
  --tab-blue-top:#4aa3ea;
  --tab-blue-bottom:#0d6fc4;
  --tab-idle:#ececec;
  --tab-idle-text:#2b6cb0;
  --label:#3b3b3b;
  --field-border:#a9a9a9;
  --field-focus:#e0a050;
  --link:#1f5fa8;
  --warn:#f26522;
  --dots:#c8c8c8;
  --icon-blue:#1f6db5;
  --muted:#9a9a9a;
}
*{box-sizing:border-box;margin:0;padding:0}
html,body{width:1200px;height:3450px;overflow:hidden;background:var(--page-bg)}
body{font-family:"Arimo",Arial,sans-serif;color:var(--label)}
.stage{position:absolute;left:0;top:0;width:320px;height:920px;transform:scale(3.75);transform-origin:0 0}
.card{position:absolute;left:10px;top:10px;width:300px;height:900px;border:1px solid var(--card-border);border-radius:12px;background:#fff}
.tab{position:absolute;top:12px;height:29px;border-radius:8px 8px 0 0;font-weight:700;font-size:13px;display:flex;align-items:center;justify-content:center;letter-spacing:.3px}
.tab--active{left:12px;width:86px;background:linear-gradient(var(--tab-blue-top),var(--tab-blue-bottom));color:#fff}
.tab--idle{background:var(--tab-idle);color:var(--tab-idle-text)}
.tab-line{position:absolute;left:12px;top:40px;width:296px;height:2px;background:var(--tab-blue-bottom)}
.label{position:absolute;left:28px;font-size:14px;font-weight:700}
.select{position:absolute;left:27px;width:223px;height:24px;border:1px solid var(--field-border);font-size:12px;padding-left:5px;display:flex;align-items:center;background:#fff}
.select--focus{border:2px solid var(--field-focus)}
.select--disabled{color:#555;background:#fafafa;border-color:#cfcfcf}
.arrow{position:absolute;right:1px;top:1px;bottom:1px;width:18px;border-left:1px solid #cfcfcf;background:linear-gradient(#fafafa,#e4e4e4);display:flex;align-items:center;justify-content:center}
.cal{position:absolute;left:29px;width:17px;height:19px}
.date{position:absolute;left:50px;width:112px;height:24px;border:1px solid var(--field-border);font-size:12px;padding-left:5px;display:flex;align-items:center}
.time{left:170px;width:80px}
.dots{position:absolute;left:22px;width:280px;border-top:2px dotted var(--dots)}
.warn{position:absolute;left:29px;top:344px;width:240px;color:var(--warn);font-size:14px;line-height:19px}
.car-visual{position:absolute;left:95px;top:385px;width:125px;height:72px;border-radius:30px 40px 18px 18px;background:radial-gradient(ellipse at 50% 40%,#6fdc2a,#2f9e0f 70%,#1f5a10)}
.link{color:var(--link);text-decoration:underline;font-size:12px}
.car-link{position:absolute;top:474px;left:0;width:320px;text-align:center}
.features{position:absolute;top:512px;left:50px}
.vip{position:absolute;top:580px;left:36px;display:flex;align-items:center}
.box{width:11px;height:11px;border:1px solid #8a8a8a;border-radius:2px;background:linear-gradient(#fff,#e9e9e9)}
.vip-name{margin-left:10px;font-size:17px;color:#2a5a8a}
.vip-more{margin-left:15px;font-size:15px;font-weight:700;color:var(--link);text-decoration:underline}
.section-title{position:absolute;left:53px;font-size:14px;font-weight:700;color:#555}
.option{position:absolute;left:31px;display:flex;align-items:center}
.option .link{margin-left:12px}
.radio{width:12px;height:12px;border:1px solid #8a8a8a;border-radius:50%;background:linear-gradient(#fff,#e5e5e5);display:flex;align-items:center;justify-content:center}
.radio--on::after{content:"";width:6px;height:6px;border-radius:50%;background:#444}
.cta{position:absolute;left:77px;top:861px;width:164px;height:41px;border-radius:9px;background:linear-gradient(#5bb2f0,#1a78d0 55%,#0f62b5);border:1px solid #0b57a3;color:#fff;font-size:19px;font-weight:700;display:flex;align-items:center;justify-content:center}
</style>
</head>
<body>
<div class="stage">
  <div class="card"></div>
  <div class="tab tab--active">STEP 1</div>
  <div class="tab tab--idle" style="left:115px;width:90px">STEP 2</div>
  <div class="tab tab--idle" style="left:222px;width:86px">STEP 3</div>
  <div class="tab-line"></div>

  <div class="label" style="top:53px">Pick-up location:</div>
  <div class="select select--focus" style="top:78px">Choose..<span class="arrow"><svg width="10" height="7"><path d="M1 1l4 4 4-4" stroke="#333" stroke-width="2" fill="none"/></svg></span></div>

  <div class="label" style="top:111px">Return location:</div>
  <div class="select" style="top:136px">Choose..<span class="arrow"><svg width="10" height="7"><path d="M1 1l4 4 4-4" stroke="#333" stroke-width="2" fill="none"/></svg></span></div>

  <div class="label" style="top:168px">Pick-up Date &amp; Time:</div>
  <svg class="cal" style="top:194px" viewBox="0 0 17 19"><rect x="0.5" y="1.5" width="16" height="17" fill="#fff" stroke="#6f8fb5"/><rect x="0.5" y="1.5" width="16" height="4" fill="#e36a3d"/><path d="M3 9h11M3 12h11M3 15h11M6 6v12M9 6v12M12 6v12" stroke="#9fb3cc" stroke-width=".8"/></svg>
  <div class="date" style="top:193px">06 Dec 2013</div>
  <div class="select time" style="top:193px">00:30<span class="arrow"><svg width="10" height="7"><path d="M1 1l4 4 4-4" stroke="#333" stroke-width="2" fill="none"/></svg></span></div>

  <div class="label" style="top:224px">Return Date &amp; Time:</div>
  <svg class="cal" style="top:250px" viewBox="0 0 17 19"><rect x="0.5" y="1.5" width="16" height="17" fill="#fff" stroke="#6f8fb5"/><rect x="0.5" y="1.5" width="16" height="4" fill="#e36a3d"/><path d="M3 9h11M3 12h11M3 15h11M6 6v12M9 6v12M12 6v12" stroke="#9fb3cc" stroke-width=".8"/></svg>
  <div class="date" style="top:249px">13 Dec 2013</div>
  <div class="select time" style="top:249px">00:30<span class="arrow"><svg width="10" height="7"><path d="M1 1l4 4 4-4" stroke="#333" stroke-width="2" fill="none"/></svg></span></div>

  <div class="dots" style="top:284px"></div>

  <div class="label" style="top:299px">Find your car:</div>
  <div class="select select--disabled" style="top:318px;left:27px;width:223px">E - Kestra 2 (or similar)<span class="arrow"><svg width="10" height="7"><path d="M1 1l4 4 4-4" stroke="#aaa" stroke-width="2" fill="none"/></svg></span></div>
  <div class="warn">Please select Pickup and return location</div>

  <div class="car-visual" role="img" aria-label="Green compact hatchback car"></div>
  <div class="car-link"><span class="link">Kestra 2 or similar</span></div>

  <svg class="features" width="225" height="40" viewBox="0 0 225 40" aria-label="Car features: 1 large bag, 2 small bags, 2 adults, 3 seats, air conditioning, automatic">
    <g fill="var(--icon-blue)">
      <path d="M10 8a5 5 0 0 1 10 0" stroke="var(--icon-blue)" stroke-width="2.5" fill="none"/>
      <rect x="2" y="9" width="30" height="25" rx="5"/>
      <text x="17" y="27" font-size="9" fill="#fff" text-anchor="middle" font-family="Arimo,Arial,sans-serif" font-weight="700">1</text>
      <path d="M52 13a4 4 0 0 1 8 0" stroke="var(--icon-blue)" stroke-width="2.2" fill="none"/>
      <rect x="45" y="14" width="23" height="20" rx="4"/>
      <text x="56.5" y="28" font-size="8" fill="#fff" text-anchor="middle" font-family="Arimo,Arial,sans-serif" font-weight="700">2</text>
      <circle cx="94" cy="8" r="7"/>
      <path d="M79 34c0-12 6-18 15-18s15 6 15 18z"/>
      <text x="94" y="30" font-size="8" fill="#fff" text-anchor="middle" font-family="Arimo,Arial,sans-serif" font-weight="700">2</text>
      <circle cx="132" cy="13" r="6"/>
      <path d="M119 34c0-10 5-15 13-15s13 5 13 15z"/>
      <text x="132" y="31" font-size="8" fill="#fff" text-anchor="middle" font-family="Arimo,Arial,sans-serif" font-weight="700">3</text>
      <g stroke="var(--icon-blue)" stroke-width="2.4">
        <path d="M170 4v26M159 10l22 14M181 10l-22 14"/>
      </g>
      <text x="183" y="37" font-size="7" text-anchor="middle" font-family="Arimo,Arial,sans-serif" font-weight="700">AC</text>
      <circle cx="209" cy="20" r="11"/>
      <text x="209" y="24.5" font-size="12" fill="#fff" text-anchor="middle" font-family="Arimo,Arial,sans-serif" font-weight="700">A</text>
    </g>
  </svg>

  <div class="dots" style="top:564px"></div>
  <div class="vip"><span class="box"></span><span class="vip-name">VIP GOLD Club</span><span class="vip-more">Learn More</span></div>
  <div class="dots" style="top:612px"></div>

  <div class="section-title" style="top:627px">Insurance Type</div>
  <div class="option" style="top:655px"><span class="radio radio--on"></span><span class="link">Comprehensive</span></div>
  <div class="option" style="top:681px"><span class="radio"></span><span class="link">Mandatory 3rd party liability</span></div>

  <div class="section-title" style="top:722px">Extras</div>
  <div class="option" style="top:751px"><span class="box"></span><span class="link">Additional driver</span></div>
  <div class="option" style="top:777px"><span class="box"></span><span class="link">Baby Seat</span></div>
  <div class="option" style="top:803px"><span class="box"></span><span class="link">Booster</span></div>
  <div class="option" style="top:829px"><span class="box"></span><span class="link">Tablet</span></div>

  <div class="cta">Get rate</div>
</div>
</body>
</html>
```